Delmer's Pressure Washing Services

Starting a pressure washing business on my own in Central Valley California, not too much experience so affordable, I do houses, fences, driveways, cars, trailers, RVs. Planning to make this full-time hoping clientele picks up after having a nice business card. Design doesn't have to be flashy, more to the point, I like simplistic/personable. I do not want something exhausting to look at or with too much going on.

Target Market(s)

Residential, Commercial

Industry/Entity Type

Pressure Washing

Contact Information for Business Card

avalible Services

Font styles to use
Sans Serif

Colors
0054AA
0677BA
7BADD7
CADEEF
E8F1F8
0094D4
00A9DD
6FCCEA
C7EBF8
E9F6FB
00AB8E
00BBA5
67D7C9
C6EFE9
E9F9F6

```html
<!DOCTYPE html>
<html lang="en">
<head>
<meta charset="UTF-8">
<title>Delmer's Pressure Washing Services – Business Card</title>
<link href="https://fonts.googleapis.com/css2?family=Montserrat:wght@400;500;600&display=swap" rel="stylesheet">
<style>
  :root {
    --navy: #0d3561;
    --sky: #2aa8f2;
    --sky-soft: #8fd0f7;
    --white: #ffffff;
    --backdrop: #eceef0;
  }
  html, body {
    margin: 0;
    padding: 0;
    width: 1200px;
    height: 1000px;
    overflow: hidden;
    background: var(--backdrop);
    font-family: "Montserrat", sans-serif;
  }
  .business-card {
    position: absolute;
    left: 312px;
    top: 319px;
    width: 581px;
    height: 348px;
    overflow: hidden;
    box-shadow: 0 6px 14px rgba(0,0,0,0.18);
  }
  .card-art {
    position: absolute;
    inset: 0;
    width: 100%;
    height: 100%;
  }
  .brand {
    position: absolute;
    right: 27px;
    top: 22px;
    text-align: right;
  }
  .brand-name {
    margin: 0;
    font-size: 26.5px;
    font-weight: 600;
    color: var(--navy);
    line-height: 1;
    letter-spacing: 0.6px;
  }
  .brand-tagline {
    margin: 4px -5px 0 0;
    font-size: 11px;
    font-weight: 500;
    color: var(--sky);
    letter-spacing: 5.4px;
  }
  .person {
    position: absolute;
    left: 32px;
    top: 136px;
  }
  .person-name {
    margin: 0;
    font-size: 25px;
    font-weight: 600;
    color: var(--white);
    line-height: 1.1;
  }
  .person-role {
    margin: 2px 0 0;
    font-size: 12.5px;
    color: var(--sky);
    letter-spacing: 5.4px;
  }
  .contact-list {
    position: absolute;
    left: 32px;
    top: 224px;
    margin: 0;
    padding: 0;
    list-style: none;
  }
  .contact-item {
    display: flex;
    align-items: center;
    height: 21px;
    font-size: 13px;
    color: var(--white);
  }
  .contact-icon {
    width: 13px;
    height: 13px;
    margin-right: 25px;
    fill: var(--sky);
  }
</style>
</head>
<body>
  <article class="business-card">
    <svg class="card-art" viewBox="0 0 581 348" xmlns="http://www.w3.org/2000/svg">
      <defs>
        <linearGradient id="wave-tone" x1="0" y1="0" x2="0" y2="1">
          <stop offset="0" stop-color="var(--sky-soft)"/>
          <stop offset="1" stop-color="var(--sky)"/>
        </linearGradient>
      </defs>
      <rect class="card-base" width="581" height="348" fill="var(--navy)"/>
      <path class="card-light-panel" fill="var(--white)"
        d="M233,0 L581,0 L581,205 C540,196 505,190 492,200 C486,252 460,282 410,284 C340,287 262,252 242,172 C229,112 226,52 233,0 Z"/>
      <rect class="wave-illustration" role="img" aria-label="Water wave with soap bubbles"
        x="300" y="148" width="281" height="128" rx="10" fill="url(#wave-tone)"/>
    </svg>

    <header class="brand">
      <p class="brand-name">YOUR LOGO</p>
      <p class="brand-tagline">YOUR TAGLINE</p>
    </header>

    <section class="person">
      <h1 class="person-name">Delmer Vance</h1>
      <p class="person-role">DESIGNATION</p>
    </section>

    <ul class="contact-list">
      <li class="contact-item">
        <svg class="contact-icon" viewBox="0 0 12 12"><path d="M6,0 C3,0 1.5,2 1.5,4.3 C1.5,7 6,12 6,12 C6,12 10.5,7 10.5,4.3 C10.5,2 9,0 6,0 Z M6,2.6 A1.7,1.7 0 1 1 6,6 A1.7,1.7 0 1 1 6,2.6 Z"/></svg>
        your state address, road 123
      </li>
      <li class="contact-item">
        <svg class="contact-icon" viewBox="0 0 12 12"><path d="M3,0 H9 A1,1 0 0 1 10,1 V11 A1,1 0 0 1 9,12 H3 A1,1 0 0 1 2,11 V1 A1,1 0 0 1 3,0 Z M3.2,1.5 V9.5 H8.8 V1.5 Z M6,10 A0.6,0.6 0 1 0 6,11.2 A0.6,0.6 0 1 0 6,10 Z"/></svg>
        +00 123 456 7890
      </li>
      <li class="contact-item">
        <svg class="contact-icon" viewBox="0 0 12 12"><path d="M2.4,0.5 L4.2,2.8 L3.2,4.2 C4,6 5.8,7.9 7.8,8.8 L9.2,7.8 L11.5,9.6 L10.2,11.5 C5.5,11 1,6.5 0.5,1.8 Z"/></svg>
        +00 123 456 789
      </li>
      <li class="contact-item">
        <svg class="contact-icon" viewBox="0 0 12 12"><path d="M0.5,2 H11.5 V10 H0.5 Z M1.6,3 L6,6.6 L10.4,3 Z M1.5,4.2 V9 H10.5 V4.2 L6,7.9 Z"/></svg>
        www.yourname@dpws.com
      </li>
    </ul>
  </article>
</body>
</html>
```